Marlow Institute Flyer Design Project

we need a flyer which promotes our business products and services, our image.

must have list of all our courses, please view our website for further information.

www.marlowinstitute.net.au

Industry/Entity Type

Business

```html
<!DOCTYPE html>
<html lang="en">
<head>
<meta charset="utf-8">
<title>Marlow Institute Flyer</title>
<link href="https://fonts.googleapis.com/css2?family=Open+Sans:ital,wght@0,400;0,600;0,700;1,800&display=swap" rel="stylesheet">
<style>
  :root {
    --navy: #0f3d8f;
    --blue: #1557b8;
    --blue-light: #2f7ad6;
    --orange: #f39a1e;
    --yellow: #fcd34a;
    --white: #ffffff;
    --photo-warm: #b98a62;
    --photo-cool: #6d8fb6;
  }
  * { box-sizing: border-box; margin: 0; padding: 0; }
  html, body { width: 896px; height: 1200px; overflow: hidden; background: #ffffff; }
  .flyer {
    position: relative;
    width: 896px;
    height: 1200px;
    overflow: hidden;
    font-family: "Open Sans", Arial, sans-serif;
    background: var(--blue);
    color: var(--white);
  }
  .hero-photo {
    position: absolute;
    top: 0; left: 0;
    width: 896px; height: 560px;
    background: linear-gradient(160deg, #e7dccd 0%, var(--photo-warm) 35%, #8a6a52 55%, var(--photo-cool) 80%, #4b6e9c 100%);
  }
  .waves { position: absolute; top: 0; left: 0; }
  .brand-badge {
    position: absolute;
    left: 596px; top: 488px;
    width: 170px; height: 170px;
    border-radius: 50%;
    background: var(--white);
    display: flex; align-items: center; justify-content: center;
    box-shadow: 0 4px 14px rgba(0,0,0,0.25);
  }
  .brand-name {
    font-weight: 700;
    font-size: 18px;
    color: var(--navy);
    text-transform: uppercase;
    text-align: center;
    line-height: 1.2;
    letter-spacing: 1px;
  }
  .headline {
    position: absolute;
    top: 670px; left: 60px; right: 60px;
    text-align: center;
    font-weight: 800;
    font-style: italic;
    font-size: 22px;
    line-height: 1.3;
    text-transform: uppercase;
  }
  .body-copy {
    position: absolute;
    top: 748px; left: 90px; right: 90px;
    text-align: center;
    font-size: 12px;
    line-height: 1.55;
  }
  .body-copy p + p { margin-top: 12px; }
  .contact {
    position: absolute;
    top: 1112px; left: 60px; right: 60px;
    text-align: center;
    font-size: 11.5px;
    font-weight: 600;
    line-height: 1.6;
  }
</style>
</head>
<body>
<div class="flyer">
  <div class="hero-photo" role="img" aria-label="Photograph of smiling students studying together at a table in front of library bookshelves"></div>

  <svg class="waves" width="896" height="1200" viewBox="0 0 896 1200" aria-hidden="true">
    <path d="M0,450 C260,530 560,480 896,400 L896,560 C600,570 300,600 0,560 Z" fill="var(--yellow)"/>
    <path d="M0,485 C280,565 580,520 896,445 L896,580 C600,600 300,620 0,580 Z" fill="var(--orange)"/>
    <path d="M0,525 C300,600 620,555 896,500 L896,1200 L0,1200 Z" fill="var(--blue)"/>
    <path d="M0,600 C300,650 620,600 896,555 L896,595 C620,635 300,690 0,650 Z" fill="var(--blue-light)" opacity="0.45"/>
  </svg>

  <div class="brand-badge">
    <div class="brand-name">Marlow<br>Institute</div>
  </div>

  <h1 class="headline">Australia enjoys a formidable global reputation<br>for its quality educational facilities.</h1>

  <div class="body-copy">
    <p>Marlow Institute is a friendly, welcoming, state-of-the-art educational facility dedicated to advancing your academic pursuits and career choices in the workforce. Our Brisbane campus is centrally located at Woolloongabba, an inner-city suburb approximately 2 kilometres from the central business district of Brisbane, the capital city of Queensland. There is easy access to accommodation, restaurants, food outlets, shops, cricket and football stadiums, learning facilities and the State library.</p>
    <p>Our Southport Campus is located in the commercial hub of the famous Gold Coast, just 80 kilometres south of Brisbane. Here students will enjoy the relaxed atmosphere of a popular tourist destination, with close access to accommodation, restaurants, food outlets, shops, sports stadiums, learning facilities and library. Both campuses are easily accessible by public transport. Marlow Institute is fully committed to continuous improvement, and our uncompromising stance on student integrity has earned us the reputation we currently enjoy. Our courses include Business, Management, Accounting, Marketing, Hospitality, Commercial Cookery, Information Technology and English language programs. Our friendly staff make every student feel welcome and supported, providing personal attention in a practical and functional learning environment, and we invite you to explore our full range of courses and start your journey with us.</p>
  </div>

  <div class="contact">
    <p>8 Grant Street Southport Queensland 4215 &bull; +61 7 5500 0000 &bull; info@marlowinstitute.net.au</p>
    <p>5 Hollis Street Woolloongabba Queensland 4102 &bull; Tel +61 7 3300 0000 &bull; www.marlowinstitute.net.au</p>
  </div>
</div>
</body>
</html>
```